Revamp QuillStoneKit.com

https://quillstonekit.com/ needs a revamp. We like the general style and colors of the site, we just want to modernize the landing page, product page, view cart page, and the final confirm page.

I'm just looking for the PSD (Photoshop files) as the deliverable.

Quick Summary
Please redesign the following Pages:
1) https://quillstonekit.com/
2) https://quillstonekit.com/rubberTracks/QuillStoneKit/400x725nx70.php (product Page)
3) https://quillstonekit.com/viewCart.php (view cart - Add something to cart to see)
4) https://quillstonekit.com/confirmShoppingCart.php (confirm cart - Add something to cart to see)

```html
<!DOCTYPE html>
<html lang="en">
<head>
<meta charset="utf-8">
<title>QuillStone Kit – Rubber Track</title>
<link href="https://fonts.googleapis.com/css2?family=Open+Sans:wght@300;400;600;700&display=swap" rel="stylesheet">
<style>
:root{
  --gold:#d9b24c;
  --gold-text:#dfa948;
  --ink:#1d1d1d;
  --text:#4a4a4a;
  --muted:#8a8a8a;
  --light:#f1f2f4;
  --line:#e3e3e3;
  --white:#fff;
  --photo:#3b3d42;
}
*{box-sizing:border-box;margin:0;padding:0}
html,body{width:1200px;height:2247px;overflow:hidden}
body{position:relative;font-family:"Open Sans",sans-serif;color:var(--text);background:var(--white)}
.abs{position:absolute}
.topbar{left:0;top:0;width:1200px;height:50px;background:#000;color:#fff;font-weight:700;font-size:19px;text-align:center;line-height:50px}
.header{left:0;top:50px;width:1200px;height:112px;background:var(--light)}
.nav a{position:absolute;top:63px;font-size:14px;color:var(--text);text-decoration:none}
.nav a.active{color:var(--gold-text)}
.currency{left:1046px;top:65px;font-size:12px;color:var(--ink)}
.logo{display:flex;align-items:center;gap:8px;font-weight:700;color:var(--ink)}
.logo .mark{width:14px;height:14px;background:var(--gold)}
.header-logo{left:112px;top:108px;font-size:28px}
.contact-phone{left:600px;width:266px;top:98px;text-align:right;color:var(--gold-text);font-size:19px;font-weight:600}
.contact-hours{left:450px;width:416px;top:125px;text-align:right;font-size:14px;font-weight:300;color:var(--text)}
.cart{left:997px;top:118px;display:flex;align-items:flex-end;gap:6px;font-size:16px;color:var(--text)}
.cart .badge{position:absolute;left:17px;top:-11px;width:18px;height:18px;border-radius:50%;background:var(--gold);color:#fff;font-size:10px;text-align:center;line-height:18px}
.categories{left:112px;top:178px;width:218px;height:41px;background:var(--gold);color:#fff;font-size:13px;font-weight:600;line-height:41px;padding-left:14px}
.search{left:364px;top:178px;width:598px;height:41px;border:1px solid #333;display:flex;align-items:center;gap:10px;padding-left:16px;font-size:13px;color:#555}
.search-btn{left:962px;top:178px;width:124px;height:41px;background:var(--gold);color:#fff;font-size:15px;text-align:center;line-height:41px}
.crumbs{left:0;top:235px;width:1200px;height:27px;background:var(--light);font-size:11px;color:var(--muted);line-height:27px;padding-left:112px}
.photo-box{background:#fff;box-shadow:0 1px 6px rgba(0,0,0,.15)}
.main-photo{left:112px;top:330px;width:471px;height:391px}
.photo-fill{position:absolute;border-radius:40px;background:radial-gradient(ellipse at center,#5a5d63 0%,var(--photo) 70%)}
.thumb{top:732px;width:150px;height:123px}
.title{left:615px;top:326px;font-size:28px;font-weight:700;color:var(--ink)}
.title small{font-size:17px;font-weight:300;color:var(--text);margin-left:18px}
.price{left:615px;top:362px;font-size:22px;font-weight:700;color:var(--gold-text)}
.stars{color:#f2b619;letter-spacing:1px}
.rating{left:615px;top:391px;font-size:10px}
.rating span{color:var(--gold-text);margin-left:4px}
.qty{left:616px;top:423px;width:100px;height:35px;display:flex;border:1px solid #ddd;font-size:14px}
.qty div{flex:1;text-align:center;line-height:33px;background:#eee}
.qty div.num{background:#fff;flex:1.2}
.add-btn{left:725px;top:423px;width:190px;height:35px;background:var(--gold);color:#fff;font-size:10px;font-weight:700;display:flex;align-items:center;justify-content:center;gap:5px}
.terms{left:615px;top:475px;font-size:13px;color:var(--ink);display:flex;align-items:center;gap:6px}
.tick{width:12px;height:12px;background:var(--gold);display:inline-flex;align-items:center;justify-content:center}
.buy-btn{left:615px;top:514px;width:300px;height:38px;background:#000;color:#fff;font-size:11px;font-weight:700;text-align:center;line-height:38px}
.desc-h{left:615px;top:604px;font-size:13px;font-weight:600;color:var(--ink)}
.desc{left:615px;width:471px;font-size:10.4px;line-height:15px;color:var(--text)}
.rule{height:1px;background:var(--line)}
.tab{left:616px;font-size:13px;color:var(--text)}
.section-title{left:0;width:1182px;top:1098px;text-align:center;font-size:24px;font-weight:700;color:var(--ink)}
.arrow{top:1102px;width:24px;height:24px;border-radius:50%;display:flex;align-items:center;justify-content:center}
.card{top:1156px;width:217px;height:303px;background:#fff;border:1px solid #e2e2e2;box-shadow:0 1px 4px rgba(0,0,0,.12);text-align:center}
.card .photo-fill{left:50px;top:30px;width:117px;height:126px}
.card .stars{position:absolute;left:0;right:0;top:176px;font-size:13px}
.card .name{position:absolute;left:0;right:0;top:197px;font-size:15px;color:#9a9a9a}
.card .cost{position:absolute;left:0;right:0;top:220px;font-size:19px;color:var(--gold-text)}
.card .btn{position:absolute;left:46px;top:251px;width:125px;height:33px;background:var(--gold);color:#fff;font-size:12px;display:flex;align-items:center;justify-content:center;gap:6px}
.callband{left:0;top:1507px;width:1200px;height:102px;background:var(--gold);color:#fff;display:flex;align-items:center;justify-content:center;gap:24px}
.callband .say{font-size:25px;font-weight:600}
.callband .num{font-size:42px;font-weight:700;margin-left:4px}
.footer-logo{left:112px;top:1700px;font-size:34px}
.divider{left:475px;top:1644px;width:1px;height:410px;background:var(--line)}
.legal{left:112px;top:1817px;width:336px;font-size:11.5px;line-height:20px;color:var(--text)}
.pay{top:2004px;width:57px;height:37px;border-radius:3px}
.subscribe{left:531px;top:1705px;font-size:15px;font-weight:700;color:var(--ink)}
.email{left:775px;top:1697px;width:311px;height:39px;border:1px solid var(--line);font-size:12px;color:#666;line-height:37px;padding-left:10px}
.col-h{top:1834px;font-size:15px;font-weight:700;color:var(--ink)}
.col{top:1870px;font-size:12.5px;line-height:27.5px;color:var(--muted)}
.col li{list-style:none;display:flex;align-items:center;gap:8px}
.follow{left:397px;top:2109px;font-size:20px;font-weight:300;color:var(--muted)}
.social{top:2100px;width:46px;height:46px;border:1.5px solid var(--gold);border-radius:50%}
.copy{left:0;top:2176px;width:1200px;height:71px;background:#f6f6f6;text-align:center;line-height:66px;font-size:16px;font-weight:300;color:var(--text)}
</style>
</head>
<body>

<div class="abs topbar">FREE SHIPPING IN THE USA</div>

<div class="abs header"></div>
<nav class="nav">
  <a class="active" style="left:113px">Home</a>
  <a style="left:173px">About Us</a>
  <a style="left:263px">Shop</a>
  <a style="left:323px">Contact Us</a>
</nav>
<div class="abs currency">USD &#8964;</div>
<div class="abs logo header-logo"><span class="mark"></span>QuillStone Kit</div>
<div class="abs contact-phone">(+1)123-456-789</div>
<div class="abs contact-hours">Timing 10:00 to 18:00 (Mon-Sat) Free By United States</div>
<div class="abs cart">
  <svg width="24" height="24" viewBox="0 0 24 24"><path fill="#1d1d1d" d="M7 18a2 2 0 1 0 0 4 2 2 0 0 0 0-4zm10 0a2 2 0 1 0 0 4 2 2 0 0 0 0-4zM1 2v2h2l3.6 7.6L5.2 14c-.1.3-.2.6-.2 1 0 1.1.9 2 2 2h12v-2H7.4l1.1-2h7.5c.8 0 1.4-.4 1.7-1l3.6-6.5L19.5 4H5.2l-.9-2H1z"/></svg>
  <span class="badge">0</span>My Cart
</div>

<div class="abs categories">CATEGORIES</div>
<div class="abs search">
  <svg width="22" height="22" viewBox="0 0 24 24"><circle cx="10" cy="10" r="7" fill="none" stroke="#d9b24c" stroke-width="2"/><path d="M15 15l6 6" stroke="#d9b24c" stroke-width="2"/></svg>
  Search Product Here...
</div>
<div class="abs search-btn">SEARCH</div>

<div class="abs crumbs">Home / shop / product detail</div>

<div class="abs photo-box main-photo">
  <div class="photo-fill" role="img" aria-label="Photo of a black rubber track loop" style="left:80px;top:45px;width:320px;height:300px"></div>
  <svg class="abs" style="left:434px;top:357px" width="18" height="18" viewBox="0 0 24 24"><circle cx="10" cy="10" r="6.5" fill="none" stroke="#222" stroke-width="2.4"/><path d="M15 15l6 6M7 10h6M10 7v6" stroke="#222" stroke-width="2.4"/></svg>
</div>
<div class="abs photo-box thumb" style="left:112px"><div class="photo-fill" role="img" aria-label="Rubber track thumbnail" style="left:35px;top:18px;width:90px;height:88px"></div></div>
<div class="abs photo-box thumb" style="left:273px"><div class="photo-fill" role="img" aria-label="Rubber track thumbnail" style="left:30px;top:18px;width:90px;height:88px"></div></div>
<div class="abs photo-box thumb" style="left:433px"><div class="photo-fill" role="img" aria-label="Rubber track thumbnail" style="left:30px;top:18px;width:90px;height:88px"></div></div>
<svg class="abs" style="left:118px;top:786px" width="10" height="14" viewBox="0 0 10 14"><path d="M8 1L2 7l6 6" fill="none" stroke="#bbb" stroke-width="2"/></svg>
<svg class="abs" style="left:563px;top:786px" width="10" height="14" viewBox="0 0 10 14"><path d="M2 1l6 6-6 6" fill="none" stroke="#222" stroke-width="2"/></svg>

<div class="abs title">Ruber Track<small>(320x86x50)</small></div>
<div class="abs price">$250</div>
<div class="abs rating"><span class="stars" style="margin:0">★★★★★</span><span>3 Reviews</span></div>
<div class="abs qty"><div>-</div><div class="num">1</div><div>+</div></div>
<div class="abs add-btn">
  <svg width="13" height="13" viewBox="0 0 24 24"><path fill="#fff" d="M7 18a2 2 0 1 0 0 4 2 2 0 0 0 0-4zm10 0a2 2 0 1 0 0 4 2 2 0 0 0 0-4zM1 2v2h2l3.6 7.6L5.2 14c-.1.3-.2.6-.2 1 0 1.1.9 2 2 2h12v-2H7.4l1.1-2h7.5c.8 0 1.4-.4 1.7-1l3.6-6.5L19.5 4H5.2l-.9-2H1z"/></svg>ADD TO CART
</div>
<div class="abs terms"><span class="tick"><svg width="9" height="9" viewBox="0 0 10 10"><path d="M1.5 5l2.5 2.5L8.5 2" fill="none" stroke="#fff" stroke-width="1.6"/></svg></span>I agree with the terms and conditions</div>
<div class="abs buy-btn">BUY NOW</div>

<div class="abs desc-h">DESCRIPTION</div>
<p class="abs desc" style="top:644px">QuillStone Kit offers premium 320x86x50 rubber tracks to keep your machinery operating at optimal performance. Our commitment to you is to make the ordering of replacement rubber tracks simple and to deliver a quality product directly to your door. The quicker we can supply your tracks, the quicker you can get your job done!</p>
<p class="abs desc" style="top:719px">Our 320x86x50 conventional rubber tracks are for use with undercarriages of machinery specifically designed to operate on rubber tracks. Conventional rubber tracks do not make contact with the metal of the equipment's rollers while in operation. No contact equals increased operator comfort. Another advantage of conventional rubber tracks is the heavy equipment roller contact will ONLY occur when aligning the conventional rubber tracks to prevent roller derailment.</p>
<p class="abs desc" style="top:824px">Our 320x86x50 conventional rubber tracks are for use with undercarriages of machinery specifically designed to operate on rubber tracks. Conventional rubber tracks do not make contact with the metal of the equipment's rollers while in operation. No contact equals increased operator comfort. Another advantage of conventional rubber tracks is the heavy equipment roller contact will ONLY occur when aligning the conventional rubber tracks to prevent roller derailment.</p>
<div class="abs rule" style="left:615px;top:933px;width:471px"></div>
<div class="abs tab" style="top:951px">ADDITIONAL INFORMATION</div>
<div class="abs rule" style="left:615px;top:991px;width:471px"></div>
<div class="abs tab" style="top:1007px">RIVEWS</div>

<div class="abs section-title">SIMILAR PRODUCTS</div>
<div class="abs arrow" style="left:1026px;background:#555"><svg width="10" height="12" viewBox="0 0 10 12"><path d="M7 1L2 6l5 5" fill="none" stroke="#fff" stroke-width="2.4"/></svg></div>
<div class="abs arrow" style="left:1061px;background:var(--gold)"><svg width="10" height="12" viewBox="0 0 10 12"><path d="M3 1l5 5-5 5" fill="none" stroke="#fff" stroke-width="2.4"/></svg></div>

<div class="abs card" style="left:112px"><div class="photo-fill" role="img" aria-label="Rubber track product photo"></div><div class="stars">★★★★★</div><div class="name">Rubber Tracks</div><div class="cost">$300</div><div class="btn"><svg width="15" height="15" viewBox="0 0 24 24"><path fill="#fff" d="M7 18a2 2 0 1 0 0 4 2 2 0 0 0 0-4zm10 0a2 2 0 1 0 0 4 2 2 0 0 0 0-4zM1 2v2h2l3.6 7.6L5.2 14c-.1.3-.2.6-.2 1 0 1.1.9 2 2 2h12v-2H7.4l1.1-2h7.5c.8 0 1.4-.4 1.7-1l3.6-6.5L19.5 4H5.2l-.9-2H1z"/></svg>ADD TO CART</div></div>
<div class="abs card" style="left:363px"><div class="photo-fill" role="img" aria-label="Rubber track product photo"></div><div class="stars">★★★★★</div><div class="name">Rubber Tracks</div><div class="cost">$300</div><div class="btn"><svg width="15" height="15" viewBox="0 0 24 24"><path fill="#fff" d="M7 18a2 2 0 1 0 0 4 2 2 0 0 0 0-4zm10 0a2 2 0 1 0 0 4 2 2 0 0 0 0-4zM1 2v2h2l3.6 7.6L5.2 14c-.1.3-.2.6-.2 1 0 1.1.9 2 2 2h12v-2H7.4l1.1-2h7.5c.8 0 1.4-.4 1.7-1l3.6-6.5L19.5 4H5.2l-.9-2H1z"/></svg>ADD TO CART</div></div>
<div class="abs card" style="left:615px"><div class="photo-fill" role="img" aria-label="Rubber track product photo"></div><div class="stars">★★★★★</div><div class="name">Rubber Tracks</div><div class="cost">$300</div><div class="btn"><svg width="15" height="15" viewBox="0 0 24 24"><path fill="#fff" d="M7 18a2 2 0 1 0 0 4 2 2 0 0 0 0-4zm10 0a2 2 0 1 0 0 4 2 2 0 0 0 0-4zM1 2v2h2l3.6 7.6L5.2 14c-.1.3-.2.6-.2 1 0 1.1.9 2 2 2h12v-2H7.4l1.1-2h7.5c.8 0 1.4-.4 1.7-1l3.6-6.5L19.5 4H5.2l-.9-2H1z"/></svg>ADD TO CART</div></div>
<div class="abs card" style="left:866px"><div class="photo-fill" role="img" aria-label="Rubber track product photo"></div><div class="stars">★★★★★</div><div class="name">Rubber Tracks</div><div class="cost">$300</div><div class="btn"><svg width="15" height="15" viewBox="0 0 24 24"><path fill="#fff" d="M7 18a2 2 0 1 0 0 4 2 2 0 0 0 0-4zm10 0a2 2 0 1 0 0 4 2 2 0 0 0 0-4zM1 2v2h2l3.6 7.6L5.2 14c-.1.3-.2.6-.2 1 0 1.1.9 2 2 2h12v-2H7.4l1.1-2h7.5c.8 0 1.4-.4 1.7-1l3.6-6.5L19.5 4H5.2l-.9-2H1z"/></svg>ADD TO CART</div></div>

<div class="abs callband">
  <svg width="42" height="42" viewBox="0 0 24 24"><path fill="#fff" d="M6.6 10.8c1.4 2.8 3.8 5.1 6.6 6.6l2.2-2.2c.3-.3.7-.4 1-.2 1.1.4 2.3.6 3.6.6.6 0 1 .4 1 1V20c0 .6-.4 1-1 1C10.6 21 3 13.4 3 4c0-.6.4-1 1-1h3.5c.6 0 1 .4 1 1 0 1.3.2 2.5.6 3.6.1.3 0 .7-.2 1l-2.3 2.2z"/></svg>
  <span class="say">if you have any question please call us</span>
  <span class="num">123-456-7890</span>
</div>

<div class="abs logo footer-logo"><span class="mark" style="width:18px;height:18px"></span>QuillStone Kit</div>
<div class="abs divider"></div>
<p class="abs legal">QuillStone Kit™, Bramwell®, Corrin®, Cartwell®, Carta®, Delvane Dig®, Garro®, Ivo®, Jarvik®, Joss Harlan®, Korvane®, Kestrel®, Moravo®, Merrow®, New Harrow®, Tavish®, Torvel®, Verlund®, and Yarrow® (hereafter, collectively referred to as "Marks") are trademarks and/or registered trademarks of their respective owners, who are individually identified in our Legal Di</p>
<div class="abs pay" style="left:113px;background:#2a4a9a" role="img" aria-label="Payment card badge"></div>
<div class="abs pay" style="left:173px;background:#c8202f" role="img" aria-label="Payment card badge"></div>
<div class="abs pay" style="left:233px;background:#e8e8e8" role="img" aria-label="Payment card badge"></div>
<div class="abs pay" style="left:294px;background:#3a8fd6" role="img" aria-label="Payment card badge"></div>

<div class="abs subscribe">SUBSCRIBE TO NEWSLETTER</div>
<div class="abs email">Enter your email address
  <svg class="abs" style="right:16px;top:11px" width="16" height="16" viewBox="0 0 24 24"><path fill="#d9b24c" d="M2 11l20-9-7 20-3-8-10-3z"/></svg>
</div>
<div class="abs rule" style="left:531px;top:1774px;width:555px"></div>

<div class="abs col-h" style="left:530px">CATEGORIES</div>
<ul class="abs col" style="left:530px"><li>Category 1</li><li>Category 2</li><li>Category 3</li><li>Category 4</li><li>Category 5</li></ul>
<div class="abs col-h" style="left:698px">QUICK LINK</div>
<ul class="abs col" style="left:698px"><li>Home</li><li>About</li><li>Privacy Policy</li><li>Terms of Service</li><li>Contact</li></ul>
<div class="abs col-h" style="left:868px;top:1838px">CONTACT US</div>
<ul class="abs col" style="left:868px;top:1873px">
  <li><svg width="14" height="14" viewBox="0 0 24 24"><path fill="#d9b24c" d="M12 2a7 7 0 0 0-7 7c0 5 7 13 7 13s7-8 7-13a7 7 0 0 0-7-7zm0 9.5a2.5 2.5 0 1 1 0-5 2.5 2.5 0 0 1 0 5z"/></svg>Lorem ipsum is dolor amet</li>
  <li><svg width="14" height="14" viewBox="0 0 24 24"><path fill="#d9b24c" d="M6.6 10.8c1.4 2.8 3.8 5.1 6.6 6.6l2.2-2.2c.3-.3.7-.4 1-.2 1.1.4 2.3.6 3.6.6.6 0 1 .4 1 1V20c0 .6-.4 1-1 1C10.6 21 3 13.4 3 4c0-.6.4-1 1-1h3.5c.6 0 1 .4 1 1 0 1.3.2 2.5.6 3.6.1.3 0 .7-.2 1l-2.3 2.2z"/></svg>(+1)123-456-789</li>
  <li><svg width="14" height="14" viewBox="0 0 24 24"><rect x="2" y="5" width="20" height="14" fill="#d9b24c"/><path d="M2 5l10 8 10-8" fill="none" stroke="#fff" stroke-width="1.5"/></svg>info@example.com</li>
</ul>

<div class="abs rule" style="left:112px;top:2079px;width:974px"></div>
<div class="abs follow">FOLLOW US:</div>
<div class="abs social" style="left:546px" role="img" aria-label="Social network link"></div>
<div class="abs social" style="left:615px" role="img" aria-label="Social network link"></div>
<div class="abs social" style="left:687px" role="img" aria-label="Social network link"></div>
<div class="abs social" style="left:757px" role="img" aria-label="Social network link"></div>

<div class="abs copy">© 2020 QUILLSTONE KIT, LLC. ALL RIGHTS ARE RESEVED.</div>

</body>
</html>
```